Norvale Email Signature Banners – Fabrication Capability Series

www.Norvale.com.au is an Australian engineering and fabrication company specialising in fabrication and welding of :
steel piping spools,
skids and frames,
small volume process steel tanks
and general steel fabrication
We require four distinct banner designs for use in Teldrin Quillmark email signatures. Each banner will highlight a specific capability while maintaining a consistent brand identity.
Deliverables
Four banners total:
Piping Spools Fabrication – focus on precision welding and stainless steel pipework
Skid & Frames Fabrication – highlight skid systems and structural frames
Small Steel Tanks Fabrication – show fabricated tanks and workshop craftsmanship
General Fabrication Solutions – broad steel fabrication theme for company-wide use
Dimensions: 600–700 px wide × 100 px high
Format: PNG (preferred), small file size prefered
Resolution: 72 dpi
Background: non-transparent, industrial or workshop setting
Text examples:
1. Piping Spools Fabrication
Option A: “Expert Fabrication Solutions for Process Piping”
Option B: “Precision Welding for Complex Systems”
Option C: “Delivering Quality in Every Spool”
Option D: “Engineered for Flow, Built for Strength”
2. Skid & Frames Fabrication
Option A: “Custom Engineered Modular Systems”
Option B: “Built Strong. Designed Smart.”
Option C: “Reliable Frames for Industrial Performance”
Option D: “Modular Fabrication for Seamless Integration”
3. Small Steel Tanks Fabrication
Option A: “Precision Built for Your Needs”
Option B: “Compact Strength. Proven Durability.”
Option C: “Fabricated for Performance and Longevity”
Option D: “Small Tanks. Big Reliability.”
4. General Fabrication Solutions
Option A: “Quality Craftsmanship, Proven Results”
Option B: “Your Partner in Precision Fabrication”
Option C: “Engineering Excellence in Every Weld”
Option D: “Australian Fabrication. Global Standards.”
Style Direction
Clean, professional, and engineering‑focused
Use Norvale brand colours
Blend photo realism with vector clarity (no heavy gradients)
Include subtle industrial textures or workshop imagery
Typography: bold sans‑serif, legible at small scale
Usage Context
These banners will appear at the bottom of staff email signatures via Quillmark Email Signature Tool for Teldrin 365, so clarity and fast loading are essential. No Logo is required in the banners.
Reference
Existing Norvale signature is attached. Colour palette to match the signature style and logo.
Target Market(s)
Engineering and construction companies,
Industry/Entity Type
Engineering fabrication design

```html
<!DOCTYPE html>
<html lang="en">
<head>
<meta charset="utf-8">
<title>Norvale Email Signature Banners – Piping Spools Fabrication</title>
<link rel="stylesheet" href="https://fonts.googleapis.com/css2?family=Figtree:wght@700;800&family=Hind:wght@600;700&display=swap">
<style>
  :root {
    --page-bg: #ffffff;
    --ink: #000000;
    --brand-blue: #1ea9e1;
    --brand-grey: #97979c;
    --banner-text: #ffffff;
    --photo-dark: #1e2f33;
    --photo-steel: #8a979b;
    --photo-light: #c9d2d4;
  }
  * { margin: 0; padding: 0; box-sizing: border-box; }
  html, body {
    width: 1200px;
    height: 1117px;
    overflow: hidden;
    background: var(--page-bg);
  }
  .sheet {
    position: relative;
    width: 1200px;
    height: 1117px;
  }
  .section-heading {
    position: absolute;
    left: 127px;
    top: 186px;
    font-family: "Figtree", sans-serif;
    font-weight: 800;
    font-size: 25px;
    line-height: 31px;
    color: var(--ink);
  }
  .banner {
    position: absolute;
    left: 250px;
    width: 700px;
    height: 100px;
    overflow: hidden;
  }
  .banner--stacked { display: flex; flex-direction: column; }
  .banner--split { display: flex; flex-direction: row; }
  .banner-photo {
    background:
      linear-gradient(180deg, rgba(30,47,51,0.15) 0%, rgba(30,47,51,0.55) 100%),
      linear-gradient(90deg, var(--photo-dark) 0%, var(--photo-steel) 25%, var(--photo-light) 50%, var(--photo-steel) 75%, var(--photo-dark) 100%);
  }
  .banner--stacked .banner-photo { height: 60px; }
  .banner--split .banner-photo { width: 293px; height: 100%; }
  .banner-tagline {
    font-family: "Hind", sans-serif;
    font-weight: 700;
    color: var(--banner-text);
  }
  .banner--stacked .banner-tagline {
    height: 40px;
    font-size: 24px;
    line-height: 40px;
    text-align: center;
    padding-top: 3px;
  }
  .banner--split .banner-tagline {
    width: 407px;
    height: 100%;
    font-size: 25px;
    line-height: 32px;
    padding: 17px 0 0 28px;
  }
  .tone-blue .banner-tagline { background: var(--brand-blue); }
  .tone-grey .banner-tagline { background: var(--brand-grey); }
  .page-number {
    position: absolute;
    left: 1157px;
    top: 1086px;
    font-family: "Figtree", sans-serif;
    font-weight: 700;
    font-size: 11px;
    color: var(--ink);
  }
</style>
</head>
<body>
<main class="sheet">
  <h1 class="section-heading">1. Piping Spools Fabrication<br>Option A: “Expert Fabrication Solutions for Process Piping”</h1>

  <section class="banner banner--stacked tone-blue" style="top:295px">
    <div class="banner-photo" role="img" aria-label="Close-up photo of stainless steel process pipework with fittings"></div>
    <p class="banner-tagline">Expert Fabrication Solutions for Process Piping</p>
  </section>

  <section class="banner banner--split tone-blue" style="top:481px">
    <p class="banner-tagline">Expert Fabrication<br>Solutions for Process Piping</p>
    <div class="banner-photo" role="img" aria-label="Photo of fabricated stainless steel piping spools and valves"></div>
  </section>

  <section class="banner banner--stacked tone-grey" style="top:658px">
    <div class="banner-photo" role="img" aria-label="Close-up photo of stainless steel process pipework with fittings"></div>
    <p class="banner-tagline">Expert Fabrication Solutions for Process Piping</p>
  </section>

  <section class="banner banner--split tone-grey" style="top:845px">
    <p class="banner-tagline">Expert Fabrication<br>Solutions for Process Piping</p>
    <div class="banner-photo" role="img" aria-label="Photo of fabricated stainless steel piping spools and valves"></div>
  </section>

  <span class="page-number">003</span>
</main>
</body>
</html>
```